Banner Ad Design Project

I have a digital X Ray blog. I need a header to fit my WP theme.
Please visit the site and let me know what you think. I am open to other design ideas not only the banner. I want the to be clean and professional.

Thank you
www.CordlessPlateScan.com

Target Market(s)

Medical Doctors, Orthopedic Surgeon, X-Ray equipment Dealers,

Industry/Entity Type

Digital

```html
<!DOCTYPE html>
<html lang="en">
<head>
<meta charset="utf-8">
<title>Wireless Digital X-ray — Flat Panel Detector</title>
<link rel="stylesheet" href="https://fonts.googleapis.com/css2?family=Arimo:wght@400;700&display=swap">
<style>
  :root {
    --ink: #2b2b27;
    --paper: #ffffff;
    --mist: #f1f4e6;
    --leaf: #8aa31b;
    --leaf-deep: #6f8812;
    --leaf-light: #b8cc4a;
    --steel: #c9cfc8;
    --steel-dark: #7d857d;
  }
  html, body {
    margin: 0;
    padding: 0;
    width: 1200px;
    height: 176px;
    overflow: hidden;
    background: var(--paper);
  }
  .banner {
    position: relative;
    width: 1200px;
    height: 176px;
    overflow: hidden;
    background: linear-gradient(90deg, var(--mist) 0%, var(--paper) 35%);
    font-family: "Arimo", Arial, sans-serif;
  }
  .banner__edge {
    position: absolute;
    left: 0; top: 0;
    width: 18px; height: 100px;
    background: linear-gradient(90deg, var(--leaf-light), transparent);
    opacity: .6;
  }
  .banner__photo {
    position: absolute;
    left: 470px; top: 0;
    width: 730px; height: 176px;
    background:
      radial-gradient(ellipse 160px 70px at 250px 95px, #eef0ea 0%, transparent 80%),
      radial-gradient(ellipse 120px 80px at 200px 90px, var(--leaf-light) 0%, transparent 75%),
      radial-gradient(ellipse 180px 90px at 560px 80px, var(--steel-dark) 0%, transparent 75%),
      linear-gradient(90deg, var(--paper) 0%, var(--steel) 45%, #e4e6e0 70%, var(--paper) 100%);
    -webkit-mask-image: linear-gradient(90deg, transparent 0%, #000 22%);
            mask-image: linear-gradient(90deg, transparent 0%, #000 22%);
  }
  .banner__band {
    position: absolute;
    left: 0; top: 0;
    width: 720px; height: 176px;
  }
  .banner__title {
    position: absolute;
    left: 30px; top: 20px;
    margin: 0;
    font-size: 40px;
    font-weight: 700;
    letter-spacing: .2px;
    color: var(--ink);
  }
  .banner__subtitle {
    position: absolute;
    left: 76px; top: 128px;
    margin: 0;
    font-size: 32px;
    font-weight: 400;
    letter-spacing: .5px;
    color: var(--paper);
  }
</style>
</head>
<body>
  <header class="banner">
    <div class="banner__edge"></div>
    <div class="banner__photo" role="img" aria-label="Photo of a green wireless flat panel X-ray detector showing a chest X-ray, with cables and a hand touching an X-ray image"></div>
    <svg class="banner__band" viewBox="0 0 720 176" aria-hidden="true">
      <defs>
        <linearGradient id="bandFill" x1="0" y1="0" x2="1" y2="0">
          <stop offset="0" stop-color="var(--leaf-deep)"/>
          <stop offset=".55" stop-color="var(--leaf)"/>
          <stop offset="1" stop-color="var(--leaf-light)" stop-opacity="0"/>
        </linearGradient>
      </defs>
      <path d="M0 104 L430 104 C520 104 560 120 600 140 C640 160 680 172 720 176 L0 176 Z" fill="url(#bandFill)"/>
    </svg>
    <h1 class="banner__title">Wireless Digital X-ray</h1>
    <p class="banner__subtitle">Flat Panel Detector</p>
  </header>
</body>
</html>
```